SipLoop Business Cards

Hi designers!

Here's some background on our start-up and this project:

SipLoop is a website that will allow users to order alcohol from nearby liquor stores and have it delivered to their homes in minutes. We are really excited to work on creating the best online, alcohol purchasing experience for the users.

So why SipLoop? We like to think of ourselves as that great friend who will get alcohol for you because he happens to have a car. We help you drink in with your friends, family, or guests. Our site will target students and young professionals (of drinking age) who are comfortable buying things online or through apps. We don't see this service as a luxury, VIP, or niche service in the least; instead, we think of us as a relaxed, service-driven start-up that believes in simple design and transparent .

Now, we want a business card that incorporates our newly acquired logo design and some complimenting colors and fonts. Feel free to do it single or double sided, although I'm a sucker for double...

If you happen to have any questions, want to throw some ideas around, or just want some feedback- email me at marco@siploop.example.

Marco Tessin
Founder

Industry/Entity Type

Business

Requirements
Must have
• Name, Position, Email, Cell-phone

No address, no fax, no land-line.

```html
<!DOCTYPE html>
<html lang="en">
<head>
<meta charset="utf-8">
<title>SipLoop Business Card</title>
<link rel="stylesheet" href="https://fonts.googleapis.com/css2?family=Open+Sans:wght@400;700&display=swap">
<style>
  :root {
    --canvas: #2b2b2b;
    --yellow: #f4c01f;
    --ink: #2a2a2a;
    --card-dark: #333333;
    --band-light: #f2f2f2;
    --band-shade: #c9c9c9;
    --white: #ffffff;
    --muted: #e6e6e6;
  }
  * { margin: 0; padding: 0; box-sizing: border-box; }
  html, body {
    width: 1200px; height: 900px; overflow: hidden;
    background: var(--canvas);
    font-family: "Open Sans", Arial, sans-serif;
  }
  .stage {
    position: relative; width: 1200px; height: 900px;
    display: flex; align-items: center; justify-content: center; gap: 40px;
  }
  .card {
    position: relative; width: 540px; height: 310px; overflow: hidden;
    box-shadow: 0 10px 30px rgba(0,0,0,.45);
  }

  /* Front */
  .card-front { background: var(--yellow); }
  .front-wordmark {
    position: absolute; left: 0; right: 0; top: 98px;
    text-align: center; font-weight: 700; font-size: 76px;
    letter-spacing: -2px; color: var(--ink); line-height: 1;
  }
  .front-footer {
    position: absolute; left: 22px; right: 22px; top: 256px;
    display: flex; align-items: center; gap: 10px;
  }
  .front-rule { flex: 1; height: 2px; background: var(--ink); }
  .front-url { font-size: 15px; color: var(--ink); letter-spacing: .5px; }

  /* Back */
  .card-back { background: var(--card-dark); }
  .holder {
    position: absolute; left: 92px; top: 40px; color: var(--white);
    line-height: 1;
  }
  .holder-name { font-size: 30px; font-weight: 400; letter-spacing: .5px; }
  .holder-role { font-size: 23px; font-weight: 400; margin-top: 2px; padding-left: 40px; color: var(--muted); }
  .contact { position: absolute; }
  .contact-label {
    font-size: 12px; color: var(--yellow); letter-spacing: .5px; margin-bottom: 8px;
  }
  .contact-line {
    display: flex; align-items: center; gap: 12px;
    font-size: 15px; color: var(--muted);
  }
  .contact-line svg { fill: var(--yellow); flex: none; }
  .contact-email { left: 318px; top: 112px; }
  .contact-phone { left: 36px; top: 162px; }
  .brand-band {
    position: absolute; left: 0; right: 0; top: 206px; bottom: 0;
    background: linear-gradient(90deg, var(--band-shade), var(--band-light) 60%, var(--white));
    overflow: hidden;
  }
  .band-wordmark {
    position: absolute; left: 14px; top: -6px;
    font-weight: 700; font-size: 132px; letter-spacing: -5px;
    line-height: 1; color: var(--ink); white-space: nowrap;
  }
</style>
</head>
<body>
<main class="stage">
  <section class="card card-front" aria-label="Business card front">
    <div class="front-wordmark">SipLoop</div>
    <div class="front-footer">
      <span class="front-rule"></span>
      <span class="front-url">www.siploop.example</span>
      <span class="front-rule"></span>
    </div>
  </section>

  <section class="card card-back" aria-label="Business card back">
    <div class="holder">
      <div class="holder-name">YOUR NAME</div>
      <div class="holder-role">Company Position</div>
    </div>

    <div class="contact contact-email">
      <div class="contact-label">EMAIL</div>
      <div class="contact-line">
        <svg width="18" height="12" viewBox="0 0 18 12" aria-hidden="true">
          <path d="M0 0h18v12H0z" />
          <path d="M1 1l8 6 8-6" fill="none" stroke="#333333" stroke-width="1.4"/>
        </svg>
        <span>youremail@domain.com</span>
      </div>
    </div>

    <div class="contact contact-phone">
      <div class="contact-label">CELL PHONE</div>
      <div class="contact-line">
        <svg width="14" height="14" viewBox="0 0 24 24" aria-hidden="true">
          <path d="M6.6 10.8a15.1 15.1 0 0 0 6.6 6.6l2.2-2.2a1 1 0 0 1 1-.25 11.4 11.4 0 0 0 3.6.57 1 1 0 0 1 1 1V20a1 1 0 0 1-1 1A17 17 0 0 1 3 4a1 1 0 0 1 1-1h3.5a1 1 0 0 1 1 1c0 1.25.2 2.45.57 3.57a1 1 0 0 1-.25 1z"/>
        </svg>
        <span>000 000 000</span>
      </div>
    </div>

    <div class="brand-band">
      <div class="band-wordmark">SipLoop</div>
    </div>
  </section>
</main>
</body>
</html>
```